Love-Drama Movie Flyer for World Sales Pitch

Dear Designers

We need for a world sales pitch a flyer for our new movie MARBLEFIN. We need a front and a back page A4.
Front: One picture we deliver for then whole page, title, some "pitch" sentences
Picture Front: https://www.fileharbor-example.net/s/qk83tnb2px71vd9/Front_Picture.jpg?dl=0
Back: Arrangement of title, 5 pictures and text we deliver (attached)

Please find in the attached examples a rough idea what we’re looking for. Should not be exactly the same.

To get an Impression of the content and style of the film, please watch the 3min teaser. This will be very important for the style of the flyer:
https://clipvault-example.net/487316920
pw: tutumarblefin

In the end we prefer a data package with the flyer made in a adobe design application for high quality print.

Thanks
Tomas Vrelnik
Producer

Target Market(s)

High profile film sales professionals

Industry/Entity Type

Film Production

Requirements
Must have
• see description
Should not have
• not too generic,
• there is the color red on the actors pullover but red is not really a color in the film. So please don't use much red
• Awards of the actor/actress are not for this movie, it's from other movies

```html
<!DOCTYPE html>
<html lang="en">
<head>
<meta charset="utf-8">
<title>MARBLEFIN – Sales Flyer</title>
<link rel="stylesheet" href="https://fonts.googleapis.com/css2?family=Alfa+Slab+One&family=Arvo:ital,wght@0,400;0,700;1,400;1,700&family=Tinos:ital,wght@0,400;1,400&display=swap">
<style>
  :root {
    --stage: #8c8c8c;
    --page: #141414;
    --white: #ffffff;
    --grey-title: #8a8a8a;
    --grey-dim: #4a4a4a;
    --grey-coming: #7a7a7a;
    --accent-red: #e3242b;
    --teal: #6fb3c4;
    --teal-deep: #2f6f86;
    --night-top: #1c3550;
    --night-low: #0d1620;
  }
  * { margin: 0; padding: 0; box-sizing: border-box; }
  html, body { width: 1200px; height: 873px; overflow: hidden; }
  body { background: var(--stage); position: relative; }

  .page {
    position: absolute; top: 56px; width: 514px; height: 726px;
    background: var(--page); overflow: hidden; color: var(--white);
    box-shadow: 0 4px 14px rgba(0,0,0,.35);
  }
  .page--front { left: 66px; }
  .page--back { left: 630px; }

  /* front */
  .hero-photo {
    position: absolute; inset: 0;
    background: radial-gradient(ellipse 40% 60% at 50% 42%, #2c2c2c 0%, #1a1a1a 55%, #121212 100%);
  }
  .cast { position: absolute; top: 24px; font-family: "Arvo", serif; font-style: italic; }
  .cast--left { left: 32px; }
  .cast--right { right: 30px; text-align: right; }
  .cast__name { font-weight: 700; font-size: 15px; color: var(--grey-title); margin-bottom: 9px; letter-spacing: .2px; }
  .award { font-size: 9.6px; line-height: 11.4px; text-transform: uppercase; margin-bottom: 9px; }
  .award small { display: block; font-size: 7.4px; line-height: 9px; }
  .award .muted { color: var(--grey-dim); }

  .tagline { position: absolute; top: 404px; font-family: "Alfa Slab One", serif; font-size: 31px; color: var(--grey-dim); }
  .tagline--a { left: 70px; }
  .tagline--b { left: 322px; }

  .title-front {
    position: absolute; top: 452px; left: 0; width: 100%; text-align: center;
    font-family: "Alfa Slab One", serif; font-size: 70px; line-height: 84px; color: var(--white); letter-spacing: 1px;
  }
  .credit { font-family: "Alfa Slab One", serif; font-size: 20px; color: var(--white); }
  .credit b { font-weight: 400; color: var(--accent-red); }
  .page--front .credit { position: absolute; top: 534px; width: 100%; text-align: center; }

  .release { position: absolute; top: 626px; font-family: "Arvo", serif; font-weight: 700; font-size: 24px; color: var(--grey-coming); letter-spacing: 7px; }
  .release--a { left: 33px; }
  .release--b { right: 14px; letter-spacing: 4px; }
  .site { position: absolute; top: 674px; width: 100%; text-align: center; font-family: "Arvo", serif; font-weight: 700; font-size: 18px; }

  /* back */
  .night-photo {
    position: absolute; left: 0; top: 0; width: 100%; height: 262px;
    background: linear-gradient(180deg, var(--night-top) 0%, #16283b 55%, var(--night-low) 85%, var(--page) 100%);
  }
  .specs { position: absolute; top: 32px; right: 36px; text-align: right; font-family: "Tinos", serif; font-size: 11.2px; line-height: 15.6px; }
  .specs__label { font-style: italic; color: var(--teal); }
  .page--back .credit { position: absolute; top: 164px; right: 38px; }
  .title-back {
    position: absolute; top: 186px; left: 0; width: 100%; text-align: center;
    font-family: "Alfa Slab One", serif; font-size: 69px; line-height: 84px; letter-spacing: 1px;
    background: linear-gradient(180deg, var(--teal) 0%, var(--teal-deep) 100%);
    -webkit-background-clip: text; background-clip: text; color: transparent;
  }
  .synopsis {
    position: absolute; top: 268px; left: 46px; width: 424px; text-align: center;
    font-family: "Tinos", serif; font-size: 10.6px; line-height: 12.4px; letter-spacing: .2px;
  }
  .still { position: absolute; top: 418px; height: 184px; }
  .still--father { left: 0; width: 303px; background: linear-gradient(120deg, #5d6a55 0%, #8a8f78 45%, #5e9aa1 100%); }
  .still--window { left: 309px; width: 205px; background: linear-gradient(100deg, #4a4743 0%, #8b8a86 55%, #c9cdc9 100%); }
  .contact {
    position: absolute; top: 620px; width: 100%; text-align: center;
    font-family: "Tinos", serif; font-style: italic; font-size: 10.8px; line-height: 12.4px; letter-spacing: .5px;
  }
  .contact__links { color: var(--accent-red); }
</style>
</head>
<body>

<section class="page page--front">
  <div class="hero-photo" role="img" aria-label="Young man in a dark hoodie and jeans standing in low light against a black background"></div>

  <div class="cast cast--left">
    <p class="cast__name">MARA ELIN VOGT</p>
    <p class="award">Meridian Award<br>Nominee 2016<br>Best Actress<small>(for Summer Lines)</small></p>
    <p class="award">Isar Film Award 2015<br>Best Young Actress<small>(for Summer Lines)</small></p>
    <p class="award">Fresh Talent Award 2012<br>Best Actress<small>(for Helena)</small></p>
  </div>

  <div class="cast cast--right">
    <p class="cast__name">JONAS KELLER</p>
    <p class="award">Alpine Film Award 2015<br>Best Actor<small>(for The Ring Road)</small></p>
    <p class="award">European Rising<br>Star 2015</p>
    <p class="award">Recurring appearance<br>in the award winning<br>US series <span class="muted">Northwatch</span></p>
  </div>

  <p class="tagline tagline--a">This is</p>
  <p class="tagline tagline--b">David.</p>
  <h1 class="title-front">MARBLEFIN</h1>
  <p class="credit">a film by <b>Lukas Brenner</b></p>
  <p class="release release--a">COMING</p>
  <p class="release release--b">FALL 2016</p>
  <p class="site">www.veridian-films.ch</p>
</section>

<section class="page page--back">
  <div class="night-photo" role="img" aria-label="Night view over a small town with fireworks and a flag in the sky"></div>

  <div class="specs">
    <p class="specs__label">Infos:</p>
    <p>Love-Drama | 110min | color |</p>
    <p>Swiss-German/German</p>
    <p>Cine 4K | 1:1,85 | Surround 5.1 |</p>
    <p>Budget: EUR 1.6 mio</p>
    <p>Release: Fall 2016</p>
  </div>

  <p class="credit">a film by <b>Lukas Brenner</b></p>
  <h2 class="title-back">MARBLEFIN</h2>

  <p class="synopsis">After the nuclear plant workers DAVID (24) and his pregnant girlfriend JESSY (22) are beaten in the main, David accesses steroids. But instead being able to preserve and to protect his girl and unborn baby, he is becoming a danger to them. Shortly before birth the amateur bodybuilder brutally beating up his love to the ground. She leaves him. Only after David has abducted his newborn daughter from the hospital, he notices his deadly dangerous trip. He brings back the child and asks Jessy to forgive him. The second film with Jonas Keller after his award winning debut on screen in THE RING ROAD side by side with the upcoming Mara Elin Vogt in the new flick of director Lukas Brenner</p>

  <div class="still still--father" role="img" aria-label="Film still: young father holding his newborn outdoors in autumn"></div>
  <div class="still still--window" role="img" aria-label="Film still: pregnant woman by a window with her partner"></div>

  <div class="contact">
    <p>Contact</p>
    <p>VeridianFilms</p>
    <p>Tomas Vrelnik |Niklas Faber</p>
    <p>Mühlegasse 14 | 8004 Zurich | Switzerland</p>
    <p>Phone: +41 79 555 01 47</p>
    <p class="contact__links">info@veridianfilms.ch | www.veridian-films.ch</p>
  </div>
</section>

</body>
</html>
```